Beer Sommelier Business Card

Dear Designers,
I'm looking forward a Beer Sommelier business card. I'm a Beer Sommelier and also a Chef in Rio de Janeiro, Brazil but this card has to be a Beer Sommelier card.
I do consulting, brigade training, tastings and harmonizations.
Forget about themes such as rock and roll, motorcycles, conventional English pubs and bellied beer drinkers. This business card will be delivered to restaurant owners and investors in Rio.
It has to seek elegance rather than luxury, and refinement rather than fashion.
I work using a black dress shirt, a Velmora Trask watch and a 18k 1981 Dorvanne aviator eyeglasses. I'm a business man and It's all part of the game.
Obviously, it has to be written in PORTUGUESE (only) and just as little as possible.

Informations to be included:

Tomas Quilbert

Beer Sommelier
Chef de Cuisine

Consultoria
Treinamento de Brigada
Degustações
Harmonizações

telephone number (just numbers): 961520387

email (just the adress): tomasquilbert@mailvessa.com

PS:
The letter "c" on both words "Degustações" and "Harmonizações" they have a small trace under it.
The letter "o" on both words "Degustações" and "Harmonizações" they have a small wave above it.

Blame the Latin.

Best Regards

Target Market(s)

Restaurant Owners and Investors. I have to impress them with my business card before I offer my services.

Industry/Entity Type

Restaurant

Contact Information for Business Card

An unique and well constructed Sommelier Business Card

Requirements
Must have
• A firts look impact. An unique and well made design. Not an ordinary product.
• Tomas Quilbert
• Beer Sommelier/Chef de Cuisine
• Consultoria
• Treinamento de Brigada
• Degustações
• Harmonizações
• telephone number (just numbers): 961520387
• email (just the adress): tomasquilbert@mailvessa.com
• PS:
• The letter "c" on both words "Degustações" and "Harmonizações" they have a small trace under it.
• The letter "o" on both words "Degustações" and "Harmonizações" they have a small wave above it.
Nice to have
• Elegance, Refinement.
• Should be a Pro Style good Looking card,
• Forget themes like beer, chef and cuisine,
• It could be a laser engraved, metal, stainless steel, PVC, Triplex, Smooth, Letterpress, all black or any other good idea.
Should not have
• Words like telephone, email, cartoon pics or glass pics.
• Should not be an ordinary card that I could download from the web or use a web program and easily make by my self.
• Just Portuguese words

```html
<!DOCTYPE html>
<html lang="pt-BR">
<head>
<meta charset="utf-8">
<title>Tomas Quilbert — Beer Sommelier</title>
<link rel="stylesheet" href="https://fonts.googleapis.com/css2?family=Cabin+Condensed:wght@400;500;600&display=swap">
<style>
  :root {
    --page: #ffffff;
    --card-light: #ddb674;
    --card-mid: #d4a862;
    --card-deep: #c99b55;
    --frame: #8c6a3e;
    --frame-line: #a88452;
    --ink: #7c6544;
    --ink-name: #a58652;
    --ink-shadow: #f0d49c;
    --ink-dark: #6a5434;
    --ornament: #b88a48;
  }
  html, body {
    margin: 0;
    padding: 0;
    width: 1200px;
    height: 702px;
    overflow: hidden;
    background: var(--page);
  }
  .card {
    position: relative;
    width: 1200px;
    height: 702px;
    font-family: "Cabin Condensed", "Arial Narrow", sans-serif;
    color: var(--ink);
  }
  .card__surface {
    position: absolute;
    left: 13px;
    top: 13px;
    width: 1175px;
    height: 678px;
    box-sizing: border-box;
    border: 4px solid var(--frame);
    border-radius: 8px;
    background:
      radial-gradient(ellipse at 30% 35%, rgba(255,235,190,0.35), transparent 60%),
      radial-gradient(ellipse at 75% 70%, rgba(180,130,60,0.18), transparent 55%),
      linear-gradient(160deg, var(--card-light), var(--card-mid) 55%, var(--card-deep));
  }
  .card__inner-rule {
    position: absolute;
    inset: 6px;
    border: 1px solid var(--frame-line);
    border-radius: 4px;
  }
  .ornament {
    position: absolute;
    border-radius: 50%;
    background: radial-gradient(ellipse at center, rgba(184,138,72,0.55), rgba(184,138,72,0.2) 55%, transparent 75%);
  }
  .ornament--left  { left: 64px;  top: 268px; width: 224px; height: 158px; }
  .ornament--right { left: 898px; top: 268px; width: 224px; height: 158px; }
  .ornament--faint { left: 1000px; top: 470px; width: 64px; height: 110px;
    background: radial-gradient(ellipse at center, rgba(184,138,72,0.3), transparent 70%); }
  .line {
    position: absolute;
    left: 0;
    width: 1200px;
    margin: 0;
    text-align: center;
    font-weight: 400;
    line-height: 1;
    text-shadow: 0 1px 0 rgba(240,212,156,0.6);
  }
  .name {
    top: 76px;
    font-size: 56px;
    font-weight: 600;
    letter-spacing: 2px;
    color: var(--ink-name);
    text-shadow: -1px -1px 0 rgba(106,84,52,0.55), 1px 1px 0 var(--ink-shadow);
  }
  .titles { top: 196px; font-size: 33px; word-spacing: 6px; }
  .titles span + span { margin-left: 14px; }
  .services-heading { top: 261px; font-size: 33px; }
  .service { font-size: 33px; letter-spacing: 0.5px; }
  .service--training { top: 349px; }
  .service--tasting  { top: 393px; }
  .service--pairing  { top: 437px; }
  .phone { top: 533px; font-size: 31px; letter-spacing: 1px; }
  .email { top: 587px; font-size: 31px; }
</style>
</head>
<body>
  <main class="card">
    <div class="card__surface">
      <div class="card__inner-rule"></div>
    </div>
    <div class="ornament ornament--left" role="img" aria-label="Ramos de trigo e lúpulo em relevo"></div>
    <div class="ornament ornament--right" role="img" aria-label="Ramos de trigo e lúpulo em relevo"></div>
    <div class="ornament ornament--faint" role="img" aria-label="Espiga de trigo em relevo suave"></div>

    <h1 class="line name">Tomas Quilbert</h1>
    <p class="line titles"><span>Beer Sommelier</span><span>Chef de Cuisine</span></p>
    <p class="line services-heading">Consultoria</p>
    <p class="line service service--training">Treinamento de Brigada</p>
    <p class="line service service--tasting">Degustações</p>
    <p class="line service service--pairing">Harmonizações</p>
    <p class="line phone">961520387</p>
    <p class="line email">tomasquilbert@mailvessa.com</p>
  </main>
</body>
</html>
```